Stationery Design Task - Stationary, memo and report templates for professional services company

Looking for someone to update stationary design but just as importantly come up with a template for reports and memos for use in our consulting firm. Would also like some brand use guidelines to be able to share with our whole team. We have an existing logo that we like. Need to update with a more contemporary look so that our deliverables to clients look good and professional yet stylish. This is for business to business communications. No need for envelope design. Important to have design for multiple pages, i.e. first page of a report and then 2nd page. Need to use in MS word documents so must be easy to use and replicate. Don't want something overly complex. Clean, fresh looking is best.

Industry/Entity Type

Information Technology

Font styles to use
Sans Serif

Colors
33a6d7
0792cd
85cae6
cee9f5
cedeed
85abd2
3377b5
0455a3

Requirements
Must have
• Clean look but with a little style or pop. Something that can easily be used in word documents. Need to have page styles that have a first page of a report (not a cover page) and then secondary page.
Nice to have
• - Although the dark blue is our primary color. Might be willing to look at some accent color as well.
Should not have
• Not just our logo on the page with a color bar.

```html
<!DOCTYPE html>
<html lang="en">
<head>
<meta charset="utf-8">
<title>Northvale Systems — Report and Letterhead Templates</title>
<link rel="stylesheet" href="https://fonts.googleapis.com/css2?family=Roboto:wght@400;700&family=Didact+Gothic&display=swap">
<style>
  :root {
    --brand-dark: #0455a3;
    --brand: #0b72c0;
    --brand-bright: #0792cd;
    --brand-light: #33a6d7;
    --brand-pale: #85cae6;
    --brand-mist: #cee9f5;
    --ink: #3c3c3c;
    --ink-soft: #555555;
    --grey-title: #a3a3a3;
    --page: #f7f7f7;
    --backdrop: #dedede;
    --tab-grey: #555a5e;
  }
  * { margin: 0; padding: 0; box-sizing: border-box; }
  html, body {
    width: 1200px; height: 578px; overflow: hidden;
    background: var(--backdrop);
  }
  .sheet {
    position: absolute; top: 52px;
    width: 338px; height: 476px;
    background: var(--page);
    box-shadow: 0 0 3px rgba(0,0,0,0.12);
    overflow: hidden;
    font-family: "Didact Gothic", "Century Gothic", sans-serif;
    color: var(--ink);
  }
  .sheet--cover { left: 61px; }
  .sheet--letter { left: 434px; }
  .sheet--continuation { left: 806px; }

  .watermark {
    position: absolute; border-radius: 50%;
    background: radial-gradient(ellipse at center, rgba(206,233,245,0.55) 0%, rgba(206,233,245,0.35) 50%, rgba(206,233,245,0) 72%);
  }
  .sheet--cover .watermark { left: 40px; top: 120px; width: 300px; height: 360px; }
  .sheet--letter .watermark { left: 100px; top: 90px; width: 250px; height: 370px; }
  .sheet--continuation .watermark { left: 50px; top: 90px; width: 290px; height: 380px; }

  /* Brand name lockups */
  .brand { position: absolute; display: flex; align-items: center; }
  .brand__dot { border-radius: 50%; background: var(--brand); flex: none; }
  .brand__name {
    font-family: "Roboto", Arial, sans-serif; font-weight: 700;
    color: var(--brand); text-transform: uppercase; line-height: 0.95;
  }
  .brand--cover { left: 46px; top: 48px; }
  .brand--cover .brand__dot { width: 58px; height: 58px; margin-right: 16px; }
  .brand--cover .brand__name { font-size: 31px; letter-spacing: 0.5px; }
  .brand--letter { left: 28px; top: 38px; }
  .brand--letter .brand__dot { width: 24px; height: 24px; margin-right: 9px; }
  .brand--letter .brand__name { font-size: 13px; }

  /* Cover */
  .cover__title {
    position: absolute; left: 0; width: 100%; top: 178px;
    text-align: center; font-family: "Roboto", Arial, sans-serif; font-weight: 700;
    font-size: 37px; color: var(--brand); letter-spacing: 0.2px;
  }
  .cover__subtitle {
    position: absolute; left: 56px; width: 226px; top: 212px;
    display: flex; align-items: center; gap: 4px;
    font-family: "Roboto", Arial, sans-serif; font-weight: 700;
    font-size: 27px; color: var(--grey-title);
  }
  .cover__subtitle::before, .cover__subtitle::after {
    content: ""; flex: 1; height: 1px; background: var(--grey-title); margin-top: 4px;
  }
  .cover__prepared {
    position: absolute; left: 0; width: 100%; top: 282px; text-align: center;
    font-family: "Roboto", Arial, sans-serif; font-weight: 700;
  }
  .cover__prepared-label { font-size: 13px; color: var(--brand); display: block; }
  .cover__prepared-name { font-size: 10px; color: var(--grey-title); display: block; margin-top: 1px; }
  .cover__description { position: absolute; left: 47px; width: 244px; top: 346px; text-align: center; }
  .cover__description h2 {
    font-family: "Roboto", Arial, sans-serif; font-weight: 700;
    font-size: 12px; color: var(--brand); line-height: 1;
  }
  .cover__description p { font-size: 5.4px; line-height: 7.6px; margin-top: 2px; color: var(--ink-soft); }
  .cover__footer {
    position: absolute; top: 450px; font-family: "Roboto", Arial, sans-serif;
    font-weight: 700; font-size: 5.6px; color: var(--ink-soft); letter-spacing: 0.1px;
  }
  .cover__footer--issued { left: 26px; }
  .cover__footer--valid { left: 209px; }

  /* Letterhead */
  .contact { position: absolute; left: 234px; top: 33px; list-style: none; font-size: 5.3px; line-height: 6.3px; color: var(--ink-soft); }
  .contact li { display: flex; align-items: flex-start; }
  .contact svg { width: 5px; height: 5px; flex: none; margin: 0.7px 3px 0 0; fill: var(--brand); }
  .contact li + li { margin-top: 0.6px; }

  .letter { position: absolute; left: 30px; width: 281px; }
  .letter__greeting { top: 134px; font-size: 8.8px; color: var(--ink); }
  .letter__body p {
    position: absolute; left: 0; width: 281px;
    font-size: 5.1px; line-height: 6.8px; text-align: justify; color: var(--ink-soft);
  }
  .letter__body { top: 158px; }
  .letter__closing { top: 311px; font-size: 5.1px; color: var(--ink-soft); }
  .signature {
    position: absolute; left: 27px; top: 330px; width: 64px; height: 28px;
    border-radius: 14px;
    background: linear-gradient(90deg, rgba(133,171,210,0.35), rgba(133,171,210,0.12));
  }

  /* Page tab */
  .page-tab { position: absolute; top: 446px; display: flex; align-items: center; height: 11px; }
  .sheet--letter .page-tab, .sheet--continuation .page-tab { left: 283px; }
  .page-tab__label {
    background: var(--tab-grey); color: #fff; font-family: "Roboto", Arial, sans-serif;
    font-size: 6px; height: 11px; line-height: 11px; padding: 0 4px; margin-right: 2px;
  }
  .page-tab__number {
    position: relative; background: var(--brand); color: #fff; font-family: "Roboto", Arial, sans-serif;
    font-size: 6px; height: 11px; line-height: 11px; width: 9px; text-align: center;
  }
  .page-tab__dot {
    position: absolute; left: 7px; top: -4px; width: 7px; height: 7px;
    border-radius: 50%; background: var(--brand-light);
  }
</style>
</head>
<body>

<!-- Report first page -->
<section class="sheet sheet--cover">
  <div class="watermark" role="img" aria-label="Faint honeycomb pattern watermark"></div>
  <div class="brand brand--cover">
    <span class="brand__dot"></span>
    <span class="brand__name">Northvale<br>Systems</span>
  </div>
  <h1 class="cover__title">REPORT TITLE</h1>
  <div class="cover__subtitle">SUB TITLE</div>
  <div class="cover__prepared">
    <span class="cover__prepared-label">REPORT PREPARED BY</span>
    <span class="cover__prepared-name">DANIEL REYES</span>
  </div>
  <div class="cover__description">
    <h2>DESCRIPTION</h2>
    <p>This report outlines our review of current systems, key findings and the steps we recommend for the year ahead. It covers scope, method, timelines and costs, with a short summary of risks and the support our team will provide during each stage of the work.</p>
  </div>
  <div class="cover__footer cover__footer--issued">PROPOSAL ISSUED: ...............................</div>
  <div class="cover__footer cover__footer--valid">PROPOSAL VALID TO: ...............................</div>
</section>

<!-- Letterhead page -->
<section class="sheet sheet--letter">
  <div class="watermark" role="img" aria-label="Faint honeycomb pattern watermark"></div>
  <div class="brand brand--letter">
    <span class="brand__dot"></span>
    <span class="brand__name">Northvale Systems</span>
  </div>
  <ul class="contact">
    <li><svg viewBox="0 0 10 10"><path d="M5 0a3.6 3.6 0 0 0-3.6 3.6C1.4 6.3 5 10 5 10s3.6-3.7 3.6-6.4A3.6 3.6 0 0 0 5 0zm0 5a1.4 1.4 0 1 1 0-2.8A1.4 1.4 0 0 1 5 5z"/></svg><span>1420 Harbor View Road<br>Fairbanks, Alaska 99701</span></li>
    <li><svg viewBox="0 0 10 10"><path d="M2 0.5l2 2-1 1.5c.6 1.3 1.6 2.3 2.9 2.9l1.5-1 2 2-1.2 1.6C4.5 9.4.6 5.5.4 1.7z"/></svg><span>555 210 4876</span></li>
    <li><svg viewBox="0 0 10 10"><path d="M0 2h10v6H0zM0.8 2.6L5 5.6l4.2-3H0.8z"/></svg><span>info@northvalesystems.com</span></li>
    <li><svg viewBox="0 0 10 10"><path d="M5 0a5 5 0 1 0 0 10A5 5 0 0 0 5 0zm0 1.2c.6.8 1 2 1.1 3.3H3.9C4 3.2 4.4 2 5 1.2zM3.9 5.5h2.2C6 6.8 5.6 8 5 8.8 4.4 8 4 6.8 3.9 5.5z"/></svg><span>www.northvalesystems.com</span></li>
  </ul>
  <p class="letter letter__greeting">Dear Mr. Reyes,</p>
  <div class="letter letter__body">
    <p style="top:0">Thank you for meeting with our team last week to discuss the network upgrade across your three regional offices. As agreed, we have reviewed the current setup, spoken with your staff and gathered the details needed to plan the next phase. This letter confirms the scope of work, the proposed schedule and the people who will lead each part of the project on our side.</p>
    <p style="top:38px">Our engineers will begin with a full audit of hardware and licences, followed by a short testing period at your main site. Work at the remaining offices will follow once the results have been reviewed and approved by your operations manager.</p>
    <p style="top:72px">We expect the full rollout to take around six weeks, with minimal disruption to daily work. Any downtime will be scheduled outside business hours and announced in advance. During this time a dedicated contact will be available to answer questions, track progress and share weekly updates. At the end of the project we will provide a written summary, updated documentation and a short training session for your staff so that the new systems can be managed with confidence.</p>
    <p style="top:116px">Please review the attached proposal and let us know if you have any questions or would like to adjust the timeline. We look forward to working with you and your team on this project.</p>
  </div>
  <p class="letter letter__closing">Sincerely,</p>
  <div class="signature" role="img" aria-label="Handwritten signature of Daniel Reyes"></div>
  <div class="page-tab">
    <span class="page-tab__label">Page</span>
    <span class="page-tab__number">1<span class="page-tab__dot"></span></span>
  </div>
</section>

<!-- Continuation page -->
<section class="sheet sheet--continuation">
  <div class="watermark" role="img" aria-label="Faint honeycomb pattern watermark"></div>
  <div class="page-tab">
    <span class="page-tab__label">Page</span>
    <span class="page-tab__number">2<span class="page-tab__dot"></span></span>
  </div>
</section>

</body>
</html>
```